Letterhead for Dorian Welk

I need a letterhead based on the business card design

Industry/Entity Type

Business

Requirements
Must have
• Footer: Dorian Welk Naturopath
Shop 4123c, 46 Carrow Lane, Sydney 2000

```html
<!DOCTYPE html>
<html lang="en">
<head>
<meta charset="utf-8">
<title>Dorian Welk Naturopath – Stationery</title>
<link rel="stylesheet" href="https://fonts.googleapis.com/css2?family=Montserrat:wght@400;500&family=Nunito:wght@600;700&display=swap">
<style>
  :root {
    --orange: #f6902a;
    --orange-soft: #f9b97a;
    --paper: #ffffff;
    --backdrop: #2e2e2e;
  }
  * { margin: 0; padding: 0; box-sizing: border-box; }
  html, body { width: 1200px; height: 1000px; overflow: hidden; }
  body {
    background: var(--backdrop);
    position: relative;
    font-family: "Nunito", sans-serif;
  }
  .sheet, .envelope { position: absolute; overflow: hidden; }

  .letterhead-front { left: 123px; top: 10px; width: 482px; height: 680px; background: var(--paper); }
  .letterhead-back  { left: 616px; top: 10px; width: 482px; height: 680px; background: var(--orange); }

  .wordmark {
    position: absolute;
    font-family: "Montserrat", sans-serif;
    font-weight: 500;
    color: var(--orange);
    text-align: center;
    white-space: nowrap;
  }
  .wordmark .name { display: block; letter-spacing: 0.02em; line-height: 1.15; }
  .wordmark .rule { display: block; height: 1px; background: currentColor; margin-left: auto; margin-right: auto; }
  .wordmark .trade { display: block; letter-spacing: 0.16em; line-height: 1.15; }

  .letterhead-front .wordmark { left: 38px; top: 48px; width: 130px; }
  .letterhead-front .name { font-size: 17px; }
  .letterhead-front .rule { width: 102px; margin-top: 14px; margin-bottom: 14px; }
  .letterhead-front .trade { font-size: 9.5px; }

  .letterhead-back .wordmark { left: 158px; top: 188px; width: 180px; color: var(--orange-soft); }
  .letterhead-back .name { font-size: 25px; }
  .letterhead-back .rule { width: 150px; margin-top: 22px; margin-bottom: 22px; }
  .letterhead-back .trade { font-size: 13px; }

  .art-placeholder { position: absolute; display: block; }
  .letterhead-front .art-placeholder { left: 300px; top: 165px; width: 182px; height: 495px; }
  .letterhead-back .art-placeholder  { left: 0; top: 225px; width: 185px; height: 440px; }

  .footer-band {
    position: absolute; left: 0; bottom: 0; width: 100%; height: 22px;
    background: var(--orange); color: var(--paper);
    font-size: 7.5px; font-weight: 700;
    display: flex; align-items: center; justify-content: center; gap: 10px;
    white-space: nowrap;
  }
  .footer-band .sep { font-weight: 600; opacity: 0.9; }

  .envelope { top: 715px; width: 491px; height: 275px; }
  .envelope-front { left: 110px; }
  .envelope-back  { left: 606px; }
  .flap { position: absolute; left: 0; top: 0; width: 100%; height: 68px; }
  .envelope-body { position: absolute; left: 0; top: 67px; width: 100%; height: 208px; }
  .envelope-front .envelope-body { background: var(--paper); }
  .envelope-back .envelope-body { background: var(--orange); }

  .envelope-front .wordmark { left: 12px; top: 36px; width: 100px; }
  .envelope-front .name { font-size: 13px; }
  .envelope-front .rule { width: 76px; margin-top: 12px; margin-bottom: 10px; }
  .envelope-front .trade { font-size: 7.5px; }
  .envelope-front .art-placeholder { left: 420px; top: 10px; width: 71px; height: 198px; }
  .envelope-back .art-placeholder  { left: 0; top: 10px; width: 79px; height: 198px; }

  .return-address {
    position: absolute; left: 25px; bottom: 14px;
    font-size: 8px; font-weight: 600; color: var(--orange);
    white-space: nowrap;
  }
</style>
</head>
<body>

  <section class="sheet letterhead-front">
    <div class="wordmark">
      <span class="name">DORIAN WELK</span>
      <span class="rule"></span>
      <span class="trade">NATUROPATHY</span>
    </div>
    <svg class="art-placeholder" viewBox="0 0 182 495" preserveAspectRatio="none" role="img" aria-label="Leaf illustration area, translucent orange leaves">
      <defs>
        <linearGradient id="artFadeLight" x1="0" y1="0" x2="0" y2="1">
          <stop offset="0" stop-color="#f9c08a" stop-opacity="0.15"/>
          <stop offset="1" stop-color="#f6a45a" stop-opacity="0.4"/>
        </linearGradient>
      </defs>
      <rect width="182" height="495" fill="url(#artFadeLight)"/>
    </svg>
    <footer class="footer-band">
      <span>Dorian Welk Naturopath</span><span class="sep">|</span>
      <span>Shop 4123c, 46 Carrow Lane, Sydney 2000</span><span class="sep">|</span>
      <span>E:dwnaturopath@mailbox.com</span><span class="sep">|</span>
      <span>P:0412 555 018</span>
    </footer>
  </section>

  <section class="sheet letterhead-back">
    <div class="wordmark">
      <span class="name">DORIAN WELK</span>
      <span class="rule"></span>
      <span class="trade">NATUROPATHY</span>
    </div>
    <svg class="art-placeholder" viewBox="0 0 185 440" preserveAspectRatio="none" role="img" aria-label="Leaf illustration area, translucent leaves over orange">
      <defs>
        <linearGradient id="artFadeDark" x1="0" y1="0" x2="0" y2="1">
          <stop offset="0" stop-color="#f9b97a" stop-opacity="0.2"/>
          <stop offset="1" stop-color="#f9b97a" stop-opacity="0.45"/>
        </linearGradient>
      </defs>
      <rect width="185" height="440" fill="url(#artFadeDark)"/>
    </svg>
  </section>

  <section class="envelope envelope-front">
    <svg class="flap" viewBox="0 0 491 68" preserveAspectRatio="none" aria-hidden="true">
      <path d="M0 68 L22 10 Q26 0 40 0 L440 0 Q462 0 472 14 L491 68 Z" fill="#f6902a"/>
    </svg>
    <div class="envelope-body">
      <div class="wordmark">
        <span class="name">DORIAN WELK</span>
        <span class="rule"></span>
        <span class="trade">NATUROPATHY</span>
      </div>
      <svg class="art-placeholder" viewBox="0 0 71 198" preserveAspectRatio="none" role="img" aria-label="Leaf illustration area, translucent orange leaves">
        <rect width="71" height="198" fill="#f9c08a" fill-opacity="0.3"/>
      </svg>
      <p class="return-address">Shop 4123c, 46 Carrow Lane, Sydney 2000</p>
    </div>
  </section>

  <section class="envelope envelope-back">
    <svg class="flap" viewBox="0 0 491 68" preserveAspectRatio="none" aria-hidden="true">
      <path d="M0 68 L18 14 Q28 0 48 0 L450 0 Q466 0 474 12 L491 68 Z" fill="#ffffff"/>
    </svg>
    <div class="envelope-body">
      <svg class="art-placeholder" viewBox="0 0 79 198" preserveAspectRatio="none" role="img" aria-label="Leaf illustration area, translucent leaves over orange">
        <rect width="79" height="198" fill="#f9b97a" fill-opacity="0.35"/>
      </svg>
    </div>
  </section>

</body>
</html>
```